Brisk Lark Delivery Service Wordpress design

My client is a delivery service whose motto is "We go where the freight leads us." Their colors are red, white and blue. They use Voyara vans and box vans - NO semi tractors. They like this Website design www.kwuzo.com, but I would like to see some designs that make them stand out. Attached is their new logo.

Target Market(s)

Businesses who use delivery services in town and anyone needing freight picked up or transported in the United States.

Industry/Entity Type

Delivery Service

Number of Pages Required

1 page

Font styles to use
Sans Serif

Colors
ec1f27
0455a3
ffffff

Requirements
Must have
• We need a Wordpress design with sliders that incorporates their new logo and the motto "WE GO WHERE THE FREIGHT LEADS US" Their corporate colors are red, white and blue. They only use voyara vans and box vans.
Nice to have
• Please use your creativity to come up with a unique design for this delivery service.
Should not have
• NO SEMI TRACTOR TRAILERS

```html
<!DOCTYPE html>
<html lang="en">
<head>
<meta charset="utf-8">
<title>Brisk Lark Delivery Service</title>
<link rel="stylesheet" href="https://fonts.googleapis.com/css2?family=Lato:wght@400;700&family=Roboto:ital,wght@0,300;0,400;0,500;0,700;1,400&display=swap">
<style>
:root{
  --red:#e8192c;
  --navy:#1f1a6b;
  --navy-dark:#1a165c;
  --ink:#1b1b1b;
  --grey-text:#8a8a8a;
  --body-text:#6a6a6a;
  --light-bg:#f4f4f6;
  --white:#ffffff;
  --rule:#e6e6e6;
}
*{box-sizing:border-box;margin:0;padding:0}
html,body{width:1200px;height:2683px;overflow:hidden}
body{position:relative;background:var(--white);font-family:"Roboto",Arial,sans-serif;color:var(--ink)}
.abs{position:absolute}

/* header */
.site-header{position:absolute;left:0;top:0;width:1200px;height:118px;background:#f7f7f7}
.brand{position:absolute;left:75px;top:34px;display:flex;align-items:center;gap:12px}
.brand-dot{width:26px;height:26px;border-radius:50%;background:var(--navy)}
.brand-name{font-family:"Lato",sans-serif;font-weight:700;font-size:28px;color:var(--navy);letter-spacing:.5px}
.login-btn{position:absolute;left:987px;top:20px;width:138px;height:34px;background:var(--red);color:var(--white);font-size:12px;font-weight:500;display:flex;align-items:center;justify-content:center;border-radius:2px}
.main-nav{position:absolute;top:80px;left:0;width:1200px;height:20px}
.main-nav a{position:absolute;font-size:12.5px;color:#333;text-decoration:none;transform:translateX(-50%);white-space:nowrap}
.main-nav a.active{color:var(--red)}
.main-nav a.active::before{content:"";position:absolute;left:50%;top:-16px;width:50px;height:3px;background:var(--red);transform:translateX(-50%)}

/* hero */
.hero{position:absolute;left:0;top:118px;width:1200px;height:585px;background:linear-gradient(135deg,#3a3d42 0%,#5c5e62 40%,#6b5a43 70%,#3b3a38 100%)}
.hero-shade{position:absolute;inset:0;background:rgba(0,0,0,.35)}
.hero-title{position:absolute;top:216px;width:100%;text-align:center;font-family:"Lato",sans-serif;font-weight:400;font-size:40px;color:var(--white);letter-spacing:.3px}
.hero-text{position:absolute;top:286px;left:190px;width:820px;text-align:center;font-size:16px;line-height:22px;color:var(--white)}
.hero-btn{position:absolute;left:524px;top:351px;width:150px;height:39px;background:var(--red);color:var(--white);font-size:13px;font-weight:500;display:flex;align-items:center;justify-content:center}
.dots{position:absolute;top:551px;left:572px;display:flex;gap:10px}
.dots span{width:11px;height:11px;border-radius:50%;border:1.5px solid var(--white)}
.dots span.on{background:var(--white)}

/* features */
.feature{position:absolute;top:779px;width:300px;text-align:center}
.feature-icon{display:block;margin:0 auto}
.feature h3{margin-top:16px;font-family:"Lato",sans-serif;font-style:italic;font-weight:400;font-size:20px;color:var(--ink)}
.feature p{margin-top:12px;font-size:13.5px;line-height:19px;color:var(--grey-text)}

/* service band */
.service{position:absolute;left:0;top:1053px;width:1200px;height:379px;background:var(--light-bg)}
.service-img{position:absolute;left:98px;top:55px;width:332px;height:278px;background:radial-gradient(ellipse at 50% 55%,#c89d66 0%,#b98a52 45%,rgba(244,244,246,0) 72%)}
.service svg.band{position:absolute;left:0;top:0}
.service-copy{position:absolute;right:75px;top:72px;width:560px;text-align:right;color:var(--white)}
.service-copy h2{font-family:"Lato",sans-serif;font-weight:400;font-size:29px;line-height:34px}
.service-copy h4{font-family:"Lato",sans-serif;font-weight:400;font-size:18px;margin-top:4px}
.service-copy p{margin-top:30px;font-size:13px;line-height:22px}
.btn-white{position:absolute;left:1007px;top:272px;width:116px;height:36px;background:var(--white);color:var(--ink);font-size:12.5px;font-weight:500;display:flex;align-items:center;justify-content:center}

/* about & delivery */
.block-title{position:absolute;top:1500px;font-family:"Roboto",sans-serif;font-weight:500;font-size:34px;line-height:38px;color:var(--ink)}
.block-title span{display:block;font-weight:300;font-size:28px;line-height:34px;color:#333}
.about-sub{position:absolute;left:75px;top:1593px;font-size:18px;font-weight:500;color:var(--red)}
.about-text{position:absolute;left:75px;top:1626px;width:492px;font-size:13px;line-height:21px;color:var(--body-text);text-align:justify}
.btn-red{position:absolute;left:75px;top:1790px;width:129px;height:36px;background:var(--red);color:var(--white);font-size:12.5px;font-weight:500;display:flex;align-items:center;justify-content:center}
.facts{position:absolute;left:651px;top:1596px;width:474px;list-style:none}
.facts li{height:55.5px;display:flex;align-items:center;border-bottom:1px solid var(--rule);font-size:16.5px;font-weight:500;color:var(--red)}
.facts li:last-child{border-bottom:none}
.facts .num{width:42px;color:#b8b8b8;font-weight:400;font-size:20px}

/* map */
.map{position:absolute;left:0;top:1901px;width:1200px;height:373px;background:linear-gradient(160deg,#d9d9d9,#e8e8e8 50%,#dcdcdc)}
.map-pin{position:absolute;left:637px;top:122px}

/* footer */
.site-footer{position:absolute;left:0;top:2274px;width:1200px;height:342px;background:var(--navy)}
.foot-col{position:absolute;top:58px}
.foot-col h5{font-size:18px;font-weight:500;color:var(--white);letter-spacing:.3px}
.foot-col ul{list-style:none;margin-top:20px}
.foot-col li{font-size:13.5px;line-height:27.5px;color:#9a98c6}
.foot-col p{margin-top:18px;font-size:13px;color:#9a98c6}
.field{position:absolute;left:853px;width:247px;height:33px;background:#e9e9ee;font-style:italic;font-size:12px;color:#333;padding:0 14px;display:flex;align-items:center}
.submit{position:absolute;left:1003px;top:2500px;width:98px;height:34px;background:var(--red);color:var(--white);font-size:12.5px;font-weight:700;display:flex;align-items:center;justify-content:center}
.bottom-bar{position:absolute;left:0;top:2616px;width:1200px;height:67px;background:var(--navy-dark);border-top:1px solid #2a2578;display:flex;align-items:center;justify-content:center;font-size:12.5px;color:#c9c8e6}
</style>
</head>
<body>

<header class="site-header">
  <div class="brand"><span class="brand-dot"></span><span class="brand-name">Brisk Lark</span></div>
  <div class="login-btn">CUSTOMER LOGIN</div>
  <nav class="main-nav">
    <a class="active" style="left:514px">HOME</a>
    <a style="left:604px">COURIER</a>
    <a style="left:694px">MEDICAL</a>
    <a style="left:786px">FREIGHT</a>
    <a style="left:882px">ABOUT US</a>
    <a style="left:989px">CONTACT US</a>
    <a style="left:1096px">CAREERS</a>
  </nav>
</header>

<section class="hero" role="img" aria-label="Photo of a courier driving a delivery van with a parcel on the seat">
  <div class="hero-shade"></div>
  <h1 class="hero-title">WE GO WHERE THE FREIGHT LEADS US</h1>
  <p class="hero-text">Lorem ipsum dolor sit amet, consectetur adipiscing elit, sed do eiusmod tempor incididunt ut labore et dolore magna aliqua. Ut enim ad minim veniam, quis nostrud exercitation</p>
  <div class="hero-btn">GET STARTED</div>
  <div class="dots"><span class="on"></span><span></span><span></span></div>
</section>

<section class="features">
  <div class="feature" style="left:90px">
    <svg class="feature-icon" width="124" height="136" viewBox="0 0 124 136">
      <path d="M62 2a60 60 0 0 1 8 119.5L62 134l-8-12.5A60 60 0 0 1 62 2z" fill="none" stroke="#e8192c" stroke-width="2"/>
      <g fill="none" stroke="#e8192c" stroke-width="2.5" stroke-linejoin="round">
        <path d="M28 46h40v30H28z"/><path d="M68 54h14l10 12v10H68z"/>
        <circle cx="40" cy="80" r="6" fill="#fff"/><circle cx="80" cy="80" r="6" fill="#fff"/>
      </g>
    </svg>
    <h3>Shipping</h3>
    <p>Here's where you can send a parcel, get express<br>shipping rates and find locations.</p>
  </div>
  <div class="feature" style="left:451px">
    <svg class="feature-icon" width="124" height="136" viewBox="0 0 124 136">
      <path d="M62 2a60 60 0 0 1 8 119.5L62 134l-8-12.5A60 60 0 0 1 62 2z" fill="none" stroke="#e8192c" stroke-width="2"/>
      <g fill="none" stroke="#e8192c" stroke-width="2.5" stroke-linejoin="round">
        <path d="M62 34l26 12v30L62 88 36 76V46z"/><path d="M36 46l26 12 26-12M62 58v30"/><path d="M49 40l26 12v10"/>
      </g>
    </svg>
    <h3>Tracking</h3>
    <p>Here's where you can send a parcel, get express<br>shipping rates and find locations.</p>
  </div>
  <div class="feature" style="left:805px">
    <svg class="feature-icon" width="124" height="136" viewBox="0 0 124 136">
      <path d="M62 2a60 60 0 0 1 8 119.5L62 134l-8-12.5A60 60 0 0 1 62 2z" fill="none" stroke="#e8192c" stroke-width="2"/>
      <g fill="none" stroke="#e8192c" stroke-width="2.5" stroke-linecap="round">
        <circle cx="62" cy="60" r="16"/><path d="M40 62a22 22 0 0 1 44 0"/>
        <rect x="36" y="58" width="8" height="14" rx="3"/><rect x="80" y="58" width="8" height="14" rx="3"/>
        <path d="M84 72c0 10-8 16-18 16"/><path d="M44 98c4-8 10-11 18-11s14 3 18 11"/>
      </g>
    </svg>
    <h3>Support</h3>
    <p>Here's where you can send a parcel, get express<br>shipping rates and find locations.</p>
  </div>
</section>

<section class="service">
  <div class="service-img" role="img" aria-label="Stack of cardboard shipping boxes"></div>
  <svg class="band" width="1200" height="379" viewBox="0 0 1200 379"><polygon points="586,0 1200,0 1200,379 474,379" fill="#e8192c"/></svg>
  <div class="service-copy">
    <h2>THE BEST CUSTOMER SERVICE</h2>
    <h4>AND OPERATIONAL EXCELLENCE</h4>
    <p>We provide the convenience of ordering: speed dialing, clarity when making the order, the speed of arrival of couriers / cars. Schedule of departments can receive from customers late postings and enables the early delivery. At the same time safe and durable packaging of any cargo we take over.</p>
  </div>
  <div class="btn-white">READ MORE</div>
</section>

<section class="about">
  <h2 class="block-title" style="left:75px">ABOUT<span>OUR COMPANY</span></h2>
  <div class="about-sub">EVERYTHING WE DO, WE DO FOR YOU</div>
  <div class="about-text">
    <p>In a rapidly changing world, there is no place for lagging behind. If you has lagged behind it probably means that you have already dropped out of life. "To be in time" - the main formula of success. We are here so that you can have time to do what is important for you.</p>
    <p style="margin-top:16px">Our role is express delivery from door to door. Delivery of documents, parcels and freight we are trusted by thousands of customers.</p>
  </div>
  <div class="btn-red">READ MORE</div>

  <h2 class="block-title" style="left:651px">DELIVERY<span>SOLUTIONS</span></h2>
  <ol class="facts">
    <li><span class="num">1.</span>EVERY DAY, MORE THAN 1,000 JORNEYS</li>
    <li><span class="num">2.</span>MORE THAN 220 MISSIONS</li>
    <li><span class="num">3.</span>27 SORTING AND DISTRIBUTION CENTERS</li>
    <li><span class="num">4.</span>MORE THAN 2 THOUSAND EMPLOYEES</li>
  </ol>
</section>

<section class="map" role="img" aria-label="Street map showing the company location">
  <svg class="map-pin" width="36" height="56" viewBox="0 0 36 56"><path d="M18 0C8 0 0 8 0 18c0 13 18 38 18 38s18-25 18-38C36 8 28 0 18 0z" fill="#e8192c"/><circle cx="18" cy="18" r="7" fill="#fff"/></svg>
</section>

<footer class="site-footer">
  <div class="foot-col" style="left:75px"><h5>INFORMATION</h5>
    <ul><li>About Us</li><li>Our Services</li><li>Company Information</li><li>Our Team</li><li>The best employees</li><li>Conference of the company</li><li>Going to take part in Summit</li></ul></div>
  <div class="foot-col" style="left:375px"><h5>DELIVERY TO..</h5>
    <ul><li>Ukraine</li><li>Russia</li><li>England</li><li>USA</li><li>Germany</li><li>France</li><li>FYR Macedonia</li></ul></div>
  <div class="foot-col" style="left:644px"><h5>TOOLS</h5>
    <ul><li>Calculator</li><li>Delivery times</li><li>Nearest branch</li><li>Work schedule</li><li>Pickup</li><li>Following</li></ul></div>
  <div class="foot-col" style="left:853px"><h5>NEWSLETTER</h5>
    <p>Sign up here for our weekly newsletter</p></div>
</footer>
<div class="field" style="top:2408px">Name</div>
<div class="field" style="top:2453px">Email Address</div>
<div class="submit">SUBMIT</div>
<div class="bottom-bar">©2016 | All Rights Reserved</div>

</body>
</html>
```